Real estate investment and development Business Visiting cards

Visiting cards for our company
We develop flats and rent them out, Now we planning to offer investors new investment opportunities in the UK Real estate sector. we used to have a design for our visiting card but we do not like it anymore. we want to have different designs keeping the same colors with our websites and company. I will attach our previous Visiting card model.

Target Market(s)

Private Investors, Banks,

Industry/Entity Type

Real Estate Development

Contact Information for Business Card

RVKT Holdings
Tomas Ferrell Director
Info to be included
3-Info

Tel
(+44 )7481 203917

Email

tomas@rvkt.co.uk

info@rvkt.co.uk

Address

17 Gorsefield Lane, Aldermoor, Westbrook, WB7 4RW

Website

rvktholdings.co.uk

Font styles to use
Serif

Colors
f78f20
fef5ee

Requirements
Must have
• The colours of the company and the Logo
Nice to have
• Modern idea and icons on the info
A code bar that directs to the website
Should not have
• a lot from the orange colour

```html
<!DOCTYPE html>
<html lang="en">
<head>
<meta charset="utf-8">
<title>RVKT Holdings – Business Card</title>
<link rel="stylesheet" href="https://fonts.googleapis.com/css2?family=PT+Serif:wght@400;700&family=Roboto:wght@400;500&display=swap">
<style>
  :root {
    --brand-orange: #f78f20;
    --ink: #111111;
    --text-grey: #4d4d4d;
    --card-white: #ffffff;
    --backdrop: #8e8e8e;
    --back-light: #bdbdbd;
    --back-dark: #050505;
  }
  * { box-sizing: border-box; margin: 0; padding: 0; }
  html, body { width: 1188px; height: 1200px; overflow: hidden; }
  body { background: var(--backdrop); position: relative; font-family: "Roboto", Arial, sans-serif; }

  .card { position: absolute; left: 246px; width: 696px; height: 386px; }
  .card-front { top: 159px; background: var(--card-white); }
  .card-back { top: 627px; background: var(--back-dark); }

  .brand { position: absolute; left: 105px; top: 164px; display: flex; align-items: center; gap: 16px; }
  .brand-square { width: 60px; height: 56px; background: var(--brand-orange); }
  .brand-name { font-family: "PT Serif", Georgia, serif; font-weight: 400; font-size: 54px; line-height: 1; color: var(--ink); letter-spacing: 0.5px; }

  .divider { position: absolute; left: 354px; top: 112px; width: 1.5px; height: 162px; background: var(--ink); }

  .person { position: absolute; left: 385px; top: 110px; }
  .person-name { font-family: "PT Serif", Georgia, serif; font-weight: 700; font-size: 20px; line-height: 1.2; color: var(--ink); text-transform: uppercase; letter-spacing: 0.3px; }
  .person-title { font-size: 17px; color: var(--brand-orange); line-height: 1.2; }

  .contact-list { position: absolute; left: 385px; top: 181px; list-style: none; }
  .contact-item { display: flex; align-items: center; height: 22.7px; font-size: 17.5px; color: var(--text-grey); white-space: nowrap; }
  .contact-icon { width: 17px; height: 17px; margin-right: 7px; flex: none; }

  .address { position: absolute; left: 0; right: 0; top: 322px; text-align: center; font-size: 17px; color: var(--text-grey); letter-spacing: 0.2px; white-space: nowrap; }
  .address-company { color: var(--brand-orange); font-weight: 500; }

  .back-pattern { position: absolute; inset: 0; background: linear-gradient(135deg, var(--back-light) 0%, #5a5a5a 22%, #1e1e1e 50%, var(--back-dark) 80%); }
</style>
</head>
<body>
  <section class="card card-front" aria-label="Business card front">
    <div class="brand">
      <div class="brand-square"></div>
      <span class="brand-name">RVKT</span>
    </div>
    <div class="divider"></div>
    <div class="person">
      <p class="person-name">Tomas Ferrell</p>
      <p class="person-title">Director</p>
    </div>
    <ul class="contact-list">
      <li class="contact-item">
        <svg class="contact-icon" viewBox="0 0 24 24"><path fill="#f78f20" d="M6.6 10.8a15.1 15.1 0 0 0 6.6 6.6l2.2-2.2c.3-.3.7-.4 1-.2 1.1.4 2.3.6 3.6.6.6 0 1 .4 1 1V20c0 .6-.4 1-1 1C10.6 21 3 13.4 3 4c0-.6.4-1 1-1h3.5c.6 0 1 .4 1 1 0 1.3.2 2.5.6 3.6.1.3 0 .7-.2 1z"/></svg>
        (+44 )7481 203917
      </li>
      <li class="contact-item">
        <svg class="contact-icon" viewBox="0 0 24 24"><rect x="2" y="5" width="20" height="14" fill="#f78f20"/><path d="M2 5l10 8 10-8M2 19l7-7M22 19l-7-7" stroke="#fff" stroke-width="1.3" fill="none"/></svg>
        tomas@rvkt.co.uk
      </li>
      <li class="contact-item">
        <svg class="contact-icon" viewBox="0 0 24 24"><rect x="2.5" y="5.5" width="19" height="13" fill="none" stroke="#f78f20" stroke-width="1.5"/><path d="M2.5 5.5l9.5 7.5 9.5-7.5M2.5 18.5l7-7M21.5 18.5l-7-7" stroke="#f78f20" stroke-width="1.3" fill="none"/></svg>
        info@rvkt.co.uk
      </li>
      <li class="contact-item">
        <svg class="contact-icon" viewBox="0 0 24 24" fill="none" stroke="#f78f20" stroke-width="1.6"><circle cx="12" cy="12" r="9.5"/><path d="M3 10c4 1 6-2 9-1s2 5 6 4M8 20c0-4 3-4 3-7M15 3.5c-1 3 2 4 5 4"/></svg>
        www.rvktholdings.co.uk
      </li>
    </ul>
    <p class="address"><span class="address-company">RVKT Holdings</span> 17 Gorsefield Lane, Aldermoor, Westbrook, WB7 4RW</p>
  </section>

  <section class="card card-back" aria-label="Business card back">
    <div class="back-pattern" role="img" aria-label="Embossed tiled brand pattern fading from light grey to black"></div>
  </section>
</body>
</html>
```